Velko's Plumbing, Heating, and AC Buisness card

I need a business card design for my Plumbing Heating and AC company. We are based out of North Windham, CT, and offer residential and light commercial services. I am looking for something that incorporates a water droplet, snowflake, and flame. I would like it to be Modern and different from a typical business card but needs to communicate confidence and security.

```html
<!DOCTYPE html>
<html lang="en">
<head>
<meta charset="utf-8">
<title>Velko's Plumbing, Heating, and AC — Business Card</title>
<link rel="stylesheet" href="https://fonts.googleapis.com/css2?family=Montserrat:wght@700;800&family=Roboto:wght@400;500;700&display=swap">
<style>
  :root {
    --backdrop: #2e2e2e;
    --card: #f1f1f1;
    --navy: #1f4f9a;
    --blue: #1c6fb5;
    --sky: #6cb8e4;
    --orange: #e08a17;
    --amber: #f0b400;
    --ink: #2a2a2a;
    --rule: #3a3a3a;
  }
  html, body {
    margin: 0;
    width: 1200px;
    height: 1138px;
    overflow: hidden;
    background: var(--backdrop);
  }
  .card {
    position: absolute;
    background: var(--card);
    border-radius: 14px;
    overflow: hidden;
    font-family: "Roboto", Arial, sans-serif;
    color: var(--ink);
  }
  .card--front { left: 274px; top: 186px; width: 622px; height: 376px; }
  .card--back  { left: 276px; top: 608px; width: 618px; height: 374px; }

  .wordmark {
    margin: 0;
    font-family: "Montserrat", Arial, sans-serif;
    font-weight: 800;
    color: var(--navy);
    letter-spacing: 1px;
    line-height: 1;
  }
  .services {
    margin: 0;
    font-family: "Montserrat", Arial, sans-serif;
    font-weight: 800;
    color: var(--orange);
    letter-spacing: 3.2px;
    line-height: 1;
  }

  /* Front */
  .front__mark {
    position: absolute;
    left: 50%; top: 72px;
    width: 104px; height: 104px;
    margin-left: -52px;
    border-radius: 50%;
    background: var(--sky);
  }
  .front__brand {
    position: absolute;
    left: 0; right: 0; top: 200px;
    text-align: center;
  }
  .front__brand .wordmark { font-size: 60px; }
  .front__brand .services { font-size: 13px; margin-top: 8px; letter-spacing: 3.6px; }
  .front__web {
    position: absolute;
    left: 0; right: 0; top: 318px;
    display: flex; align-items: center; justify-content: center; gap: 22px;
    font-size: 16px;
  }
  .front__web .rule {
    width: 72px; height: 2px; background: var(--rule); border-radius: 2px;
  }
  .front__band {
    position: absolute; left: 0; right: 0; bottom: 0; height: 17px;
    display: flex;
  }
  .front__band .band-blue { flex: 1; background: linear-gradient(90deg, var(--blue), #0f4b93); }
  .front__band .band-orange { flex: 1; background: linear-gradient(90deg, #de7d1a, var(--amber)); }

  /* Back */
  .back__brand { position: absolute; left: 42px; top: 44px; }
  .back__brand .wordmark { font-size: 50px; }
  .back__brand .services { font-size: 11px; margin-top: 6px; letter-spacing: 3px; }

  .back__person { position: absolute; left: 42px; top: 146px; }
  .person__name { margin: 0; font-size: 23px; font-weight: 700; color: var(--blue); }
  .person__role { margin: 4px 0 0; font-size: 16px; }

  .contact {
    position: absolute; left: 42px; top: 222px;
    margin: 0; padding: 0; list-style: none;
    font-size: 16px; line-height: 26px;
  }
  .contact li { display: flex; align-items: center; }
  .contact svg { width: 14px; height: 14px; margin-right: 17px; fill: var(--orange); }
  .contact .address { display: block; }

  .back__mark {
    position: absolute; right: 14px; top: 60px;
    width: 290px; height: 290px;
    border-radius: 50%;
    background: var(--sky);
  }
</style>
</head>
<body>

<section class="card card--front" aria-label="Card front">
  <div class="front__mark" aria-hidden="true"></div>
  <div class="front__brand">
    <h1 class="wordmark">VELKO'S</h1>
    <p class="services">PLUMBING | HEATING | AC</p>
  </div>
  <div class="front__web">
    <span class="rule"></span>
    <span>www.velkoplumbing.com</span>
    <span class="rule"></span>
  </div>
  <div class="front__band">
    <span class="band-blue"></span>
    <span class="band-orange"></span>
  </div>
</section>

<section class="card card--back" aria-label="Card back">
  <div class="back__brand">
    <h2 class="wordmark">VELKO'S</h2>
    <p class="services">PLUMBING | HEATING | AC</p>
  </div>

  <div class="back__person">
    <p class="person__name">Marko Velkov</p>
    <p class="person__role">Managing Director</p>
  </div>

  <ul class="contact">
    <li>
      <svg viewBox="0 0 16 16" aria-hidden="true"><path d="M2 5c0-2 2-3 6-3s6 1 6 3v1h-3V5H5v1H2zM4 7h8l2 7H2z"/></svg>
      860-555-0142
    </li>
    <li>
      <svg viewBox="0 0 16 16" aria-hidden="true"><path d="M1 3h14v10H1zM2 4l6 5 6-5v-0.2H2z" fill-rule="evenodd"/></svg>
      marko@velkoplumbing.com
    </li>
    <li>
      <svg viewBox="0 0 16 16" aria-hidden="true"><circle cx="8" cy="8" r="7"/></svg>
      www.velkoplumbing.com
    </li>
    <li class="address">18 Maple Row, Elm Hollow,<br>Fairbrook, US 06201</li>
  </ul>

  <div class="back__mark" aria-hidden="true"></div>
</section>

</body>
</html>
```